Retail and Ecommerce Archery Shop needs new Home Page Design

We need a homepage design created for an existing company named Redhollow Bowsport Hub. They sell various types of Archery equipment for both Bow hunting and Target shooting both in store and online. They offer shooting lessons, have an indoor archery shooting range with memberships available, and have their own line of bowstrings. For color scheme, use the current home page as inspiration. The Homepage Template has links to specific images, if any other images are needed, stock images are acceptable.

Current Website: https://rhbowsporthub.com/

Customer Avatar: https://files.quillnest.net/page/d/4Tq8Wm2RbXk9LpZ3vNc7HyF1gJd6sKe5uA0oVtB2/view?mode=shared

Core Message Canvas: https://files.quillnest.net/tables/d/7Hm_482rTz906R3k21wLuNy8Pq0Zc47bd5jS2X_vW/view?mode=shared

Homepage Template-Use this worksheet as the structue of the homepage: https://files.quillnest.net/page/d/9xkpWvRfa2B5nT7eLcM3JsYq0HdG8oUiZbN4/view?mode=shared

```html
<!DOCTYPE html>
<html lang="en">
<head>
<meta charset="utf-8">
<title>Redhollow Bowsport Hub – Home</title>
<link href="https://fonts.googleapis.com/css2?family=Cinzel:wght@500;600&family=Jost:wght@400;500;600&display=swap" rel="stylesheet">
<style>
:root{
  --red:#e31e24;
  --red-deep:#b5121b;
  --blue:#0a7dc2;
  --yellow:#f5c400;
  --black:#0d0d0d;
  --ink:#1c1c1c;
  --grey-bg:#f4f4f4;
  --panel:#232323;
  --white:#fff;
}
*{margin:0;padding:0;box-sizing:border-box}
html,body{width:1200px;height:4244px;overflow:hidden}
body{font-family:"Jost",sans-serif;color:var(--ink);background:var(--white);position:relative}
.abs{position:absolute}
.serif{font-family:"Cinzel",serif;font-weight:500;letter-spacing:.5px}
.btn{position:absolute;display:flex;align-items:center;justify-content:center;color:var(--white);font-size:9px;font-weight:600;letter-spacing:4px;text-transform:uppercase;border-left:4px solid var(--yellow)}
.btn.red{background:var(--red)}
.btn.blue{background:var(--blue)}
.btn.white{background:var(--white);color:var(--ink)}

/* header */
.site-header{position:absolute;left:0;top:0;width:1200px;height:115px;background:var(--black)}
.brand{position:absolute;left:108px;top:26px;display:flex;align-items:center;gap:12px}
.brand-dot{width:34px;height:34px;border-radius:50%;background:var(--yellow)}
.brand-name{font-family:"Cinzel",serif;font-weight:600;color:var(--yellow);font-size:20px;line-height:1.1}
.search{position:absolute;left:812px;top:10px;width:210px;height:24px;border-bottom:1px solid #444;color:#ccc;font-size:9px;padding-top:6px;padding-left:8px}
.search-icon{position:absolute;left:995px;top:11px;width:20px;height:20px;border-radius:50%;background:var(--yellow)}
.cart-icon{position:absolute;left:1047px;top:11px;width:20px;height:20px;border-radius:50%;background:var(--yellow)}
.nav-bar{position:absolute;left:350px;top:52px;width:850px;height:63px;background:var(--white);clip-path:polygon(22px 0,100% 0,100% 100%,0 100%)}
.nav{position:absolute;top:77px;display:flex;gap:0;font-size:12px;font-weight:500;text-transform:uppercase}
.nav a{position:absolute;color:var(--ink);text-decoration:none;white-space:nowrap}
.nav-contact{left:953px;top:68px;width:115px;height:30px}

/* hero */
.hero{position:absolute;left:0;top:115px;width:1200px;height:656px;background:linear-gradient(180deg,#3d3a33 0%,#2a2a24 40%,#3a3550 75%,#2b2638 100%)}
.hero h1{position:absolute;left:0;top:375px;width:1200px;text-align:center;color:var(--white);font-size:56px;line-height:60px}
.hero .tag{position:absolute;left:0;top:502px;width:1200px;text-align:center;color:var(--white);font-size:13px;font-weight:500}
.scroll-line{position:absolute;left:1111px;top:83px;width:1px;height:486px;background:rgba(255,255,255,.5)}
.scroll-mouse{position:absolute;left:1104px;top:318px;width:14px;height:20px;border:1.5px solid #fff;border-radius:7px;background:#2e2b27}

/* pro shop */
.pro h2{position:absolute;left:198px;top:878px;font-size:34px;line-height:42px;width:340px}
.badge{position:absolute;width:124px;height:70px;background:var(--white);box-shadow:0 6px 20px rgba(0,0,0,.1);display:flex;align-items:center;justify-content:center}
.badge span{width:70px;height:22px;border-radius:11px;background:#d8d8d8}
.pro p{position:absolute;left:198px;top:1071px;width:600px;font-size:12px;line-height:20px;color:#333}
.gallery div{position:absolute;top:1178px;height:312px}

/* bowstrings */
.strings{position:absolute;left:0;top:1574px;width:1200px;height:804px;background:radial-gradient(ellipse at 40% 45%,#d81f27 0%,var(--red-deep) 75%)}
.strings h2{position:absolute;left:0;top:70px;width:1200px;text-align:center;color:var(--white);font-size:50px;line-height:60px}

/* welcome */
.welcome h2{position:absolute;left:0;top:2452px;width:1200px;text-align:center;font-size:52px;line-height:58px}
.welcome .sub{position:absolute;left:0;top:2571px;width:1200px;text-align:center;font-size:12px;font-weight:500;text-transform:uppercase}
.acc{position:absolute;left:198px;width:392px;background:var(--grey-bg);padding:0 0 0 66px;font-size:11px;font-weight:600;text-transform:uppercase;line-height:18px}
.acc .num{position:absolute;left:22px;width:22px;height:22px;border-radius:50%;background:var(--blue);color:#fff;font-size:7px;display:flex;align-items:center;justify-content:center;box-shadow:0 0 0 4px #d6e9f5}
.acc.open{background:var(--white);box-shadow:0 4px 18px rgba(0,0,0,.1)}
.acc.open p{font-size:9.5px;font-weight:400;text-transform:none;line-height:14.5px;color:#444;margin-top:6px;padding-right:22px}
.acc-line{position:absolute;left:32px;top:40px;width:1px;height:110px;background:var(--blue)}

/* newsletter */
.community{position:absolute;left:0;top:3103px;width:1200px;height:663px;background:var(--grey-bg)}
.community h2{position:absolute;left:198px;top:76px;font-size:36px;line-height:42px}
.community .lead{position:absolute;left:659px;top:90px;width:320px;padding-left:14px;border-left:2px solid var(--red);font-size:12.5px;line-height:20px;color:#444}
.news-card{position:absolute;left:540px;top:238px;width:462px;height:298px;background:var(--white);box-shadow:0 6px 22px rgba(0,0,0,.07)}
.news-card h3{position:absolute;left:50px;top:50px;width:360px;font-size:12.5px;font-weight:500;line-height:18px}
.field{position:absolute;left:50px;width:363px;height:38px;background:var(--grey-bg);border:1px solid #e2e2e2;font-size:8px;color:#666;padding:14px 0 0 24px}

/* footer */
.footer{position:absolute;left:0;top:3766px;width:1200px;height:428px;background:var(--black);color:#fff}
.footer .brand{left:198px;top:112px}
.footer .about{position:absolute;left:198px;top:222px;width:225px;font-size:9.5px;line-height:16px;color:#ddd}
.social{position:absolute;top:322px;width:26px;height:26px;border-radius:50%;background:var(--red)}
.flinks a{position:absolute;left:517px;color:#fff;font-size:9.5px;text-decoration:none;text-transform:uppercase}
.contact-box{position:absolute;left:725px;top:104px;width:277px;height:244px;background:var(--panel)}
.c-item{position:absolute;left:65px;font-size:9.5px;line-height:14px}
.c-item small{display:block;font-size:6px;letter-spacing:.5px;color:#bbb}
.c-icon{position:absolute;left:32px}
.bottom-bar{position:absolute;left:0;top:4194px;width:1200px;height:50px;background:#1a1a1a;color:#ccc;font-size:9px}
</style>
</head>
<body>

<header class="site-header">
  <div class="brand"><span class="brand-dot"></span><span class="brand-name">Redhollow<br>Bowsport Hub</span></div>
  <div class="search">SEARCH...</div>
  <span class="search-icon"></span>
  <span class="cart-icon"></span>
  <div class="nav-bar"></div>
</header>
<nav class="nav">
  <a style="left:403px">Shop</a>
  <a style="left:480px">About Us</a>
  <a style="left:584px">Range</a>
  <a style="left:670px">Pro Shop</a>
  <a style="left:776px">Electric Bowstrings</a>
</nav>
<div class="btn red nav-contact">Contact</div>

<section class="hero" role="img" aria-label="Bow hunter in camouflage drawing a compound bow in a forest with purple wildflowers">
  <h1 class="serif">YOUR BOW HUNTING<br>ADVENTURE STARTS HERE!</h1>
  <div class="tag">TOP-NOTCH EQUIPMENT - EXPERTISE - UNMATCHED SUPPORT</div>
  <div class="scroll-line"></div>
  <div class="scroll-mouse"></div>
</section>
<div class="btn blue" style="left:369px;top:659px;width:223px;height:28px">Indoor Archery Range</div>
<div class="btn red" style="left:608px;top:659px;width:223px;height:28px">Shop Our Bows</div>

<section class="pro">
  <h2 class="serif">WE ARE A FULL-SERVICE ARCHERY PRO SHOP</h2>
  <div class="badge" style="left:590px;top:857px"><span></span></div>
  <div class="badge" style="left:733px;top:857px"><span></span></div>
  <div class="badge" style="left:873px;top:857px"><span></span></div>
  <div class="badge" style="left:565px;top:944px"><span></span></div>
  <div class="badge" style="left:705px;top:944px"><span></span></div>
  <div class="badge" style="left:847px;top:944px"><span></span></div>
  <p>Our Services Include Bow Setup And Sizing, D-Loop And Peep Sight Installs, Accessory Installs, And Setup, Cam/Limb Swaps, String Swaps, Paper Tuning, 2nd/3rd Axis Adjustments, Replacement Parts, Arrow Building, Tuning, And Much More!</p>
  <div class="btn blue" style="left:880px;top:1084px;width:122px;height:30px">Shop Now</div>
  <div class="gallery">
    <div role="img" aria-label="Technician working at the bow service bench" style="left:198px;width:255px;background:linear-gradient(160deg,#5a4a3c,#2a2520)"></div>
    <div role="img" aria-label="Staff behind the counter with arrows on the wall" style="left:473px;width:254px;background:linear-gradient(160deg,#c9a878,#6e6050)"></div>
    <div role="img" aria-label="Staff member holding a compound bow in the shop" style="left:747px;width:255px;background:linear-gradient(160deg,#c7a27a,#4d4740)"></div>
    <div role="img" aria-label="Archery event stage with lights" style="left:1022px;width:178px;background:linear-gradient(160deg,#3a3a44,#151518)"></div>
  </div>
</section>

<section class="strings">
  <h2 class="serif">OUR CUSTOM ELECTRIC<br>BOWSTRINGS</h2>
  <svg class="abs" style="left:239px;top:217px" width="722" height="430" viewBox="0 0 722 430">
    <rect x="66" y="0" width="590" height="380" rx="20" fill="#d9d9db"/>
    <rect x="89" y="24" width="544" height="301" fill="#222"/>
    <rect x="0" y="380" width="722" height="20" rx="4" fill="#e4e4e6"/>
    <path d="M0 400 H722 L700 416 H22 Z" fill="#a9a9ad"/>
    <rect x="100" y="356" width="522" height="22" fill="#2a2a2c"/>
  </svg>
  <div class="abs" role="img" aria-label="Video still of a bowstring spinning on a red serving machine" style="left:328px;top:241px;width:544px;height:301px;background:linear-gradient(120deg,#8a8e92 0%,#c0c3c6 40%,#b3232a 70%,#5a1014 100%)"></div>
  <svg class="abs" style="left:580px;top:372px" width="40" height="40" viewBox="0 0 40 40"><circle cx="20" cy="20" r="20" fill="#fff"/><path d="M15 11 L29 20 L15 29 Z" fill="var(--blue)"/></svg>
  <div class="btn white" style="left:458px;top:690px;width:282px;height:30px">Shop Our Custom Bowstrings</div>
</section>

<section class="welcome">
  <h2 class="serif">WELCOME TO YOUR LOCAL<br>ARCHERY SHOP</h2>
  <div class="sub">Where Consistency Is Built</div>
  <div class="acc" style="top:2630px;height:69px;padding-top:26px"><span class="num" style="top:24px">01</span>Looking For A New Bow Setup?</div>
  <div class="acc" style="top:2714px;height:71px;padding-top:18px"><span class="num" style="top:24px">02</span>Are You Looking To Improve Your Shot?<br>Reserve Some Time On Our Range!</div>
  <div class="acc open" style="top:2798px;height:165px;padding-top:22px"><span class="num" style="top:24px">03</span><span class="acc-line"></span>Are You Looking To Improve Your Shot?<br>Reserve Some Time On Our Range!
    <p>Before you step into the field to take your first shot of the season, take time to go to the range. Archery, like any skill, requires practice &amp; diligence to develop a consistent &amp; confident shot. We have a 12-lane 20-yard indoor range in the shop. Daily Range and memberships are available. We also offer bow rental and lessons.</p></div>
  <div class="btn red" style="left:198px;top:2986px;width:222px;height:30px">Range Informaiton</div>
  <div class="abs" role="img" aria-label="Two hunters with packs climbing a rocky ridge under a pale sky" style="left:638px;top:2630px;width:364px;height:387px;background:linear-gradient(180deg,#a8bfd4 0%,#8e9aa6 45%,#3c3a38 75%,#1e1e1e 100%)"></div>
</section>

<section class="community">
  <h2 class="serif">JOIN OUR ARCHERY<br>COMMUNITY</h2>
  <div class="lead">Join Today &amp; Stay Up-To-Date On New Product Releases, Shop Promotions, And Our Archery Newsletters</div>
  <div class="abs" role="img" aria-label="Archer in camouflage drawing a recurve bow in the woods" style="left:198px;top:198px;width:374px;height:379px;background:linear-gradient(150deg,#6b4a2e 0%,#4a3622 50%,#2c2218 100%)"></div>
  <div class="news-card">
    <h3>EXCLUSIVE DEALS, TIPS, AND UPDATES STRAIGHT TO YOUR INBOX!</h3>
    <div class="field" style="top:105px">Name</div>
    <div class="field" style="top:153px">Email</div>
    <div class="btn blue" style="left:50px;top:220px;width:244px;height:32px">Subscribe Our Newsletter</div>
  </div>
</section>

<footer class="footer">
  <div class="brand"><span class="brand-dot"></span><span class="brand-name">Redhollow<br>Bowsport Hub</span></div>
  <p class="about">Lorem Ipsum is simply dummy text of the printing and typesetting industry. Lorem Ipsum has been the industry's standard dummy text ever since the 1500s.</p>
  <span class="social" style="left:198px"></span>
  <span class="social" style="left:238px"></span>
  <div class="flinks">
    <a style="top:146px">Shop</a>
    <a style="top:191px">About Us</a>
    <a style="top:235px">Range</a>
    <a style="top:280px">Pro Shop</a>
    <a style="top:324px">Electric Bowstrings</a>
  </div>
  <div class="contact-box">
    <svg class="c-icon" style="top:34px" width="14" height="11" viewBox="0 0 14 11"><rect x=".5" y=".5" width="13" height="10" fill="#fff"/><path d="M.5 .5 L7 6 L13.5 .5" stroke="#232323" fill="none"/></svg>
    <div class="c-item" style="top:28px"><small>MAIL</small>hello@redhollowbowsport.com</div>
    <svg class="c-icon" style="top:96px" width="14" height="14" viewBox="0 0 14 14"><path d="M14 0 L0 6 L6 8 L8 14 Z" fill="#fff"/></svg>
    <div class="c-item" style="top:92px;width:190px"><small>ADDRESS</small>Unit 4 &amp; 5 Fernbrook Lodge Millstone Trade Park Ashgrove Way Redhollow RH4 2TL</div>
    <svg class="c-icon" style="top:184px" width="14" height="14" viewBox="0 0 14 14"><path d="M3 0 L6 4 L4.5 6 Q6 9 8 9.5 L10 8 L14 11 L12 14 Q4 13 0 3 Z" fill="#fff"/></svg>
    <div class="c-item" style="top:180px"><small>PHONE</small>+44 (0)123 480 6159</div>
  </div>
</footer>
<div class="bottom-bar">
  <span class="abs" style="left:198px;top:19px">© Copyright © 2023 Fernbrook Holdings. All Rights Reserved.</span>
  <span class="abs" style="left:840px;top:19px">Terms Of Service &nbsp; | &nbsp; Privacy Policy</span>
</div>

</body>
</html>
```